Disability Support service provider Needs a shopfront graphic Design

We are based in Sydney, Australia. Our company is called 'Bright Harbour Care Services'. We provide care services to anyone with a disability. I would like to see designs that are colourful and perhaps transparent. The colours from my logo uploaded can be used as a guide. I would also like a bit of information about our services on the design somewhere maybe in point form, for eg. Disability Support Services, We are people helping People, take control of your disability, supporting people to live the life they want to live, I would like the design to be friendly and inviting.

```html
<!DOCTYPE html>
<html lang="en">
<head>
<meta charset="UTF-8">
<title>Bright Harbour Care Services – Shopfront</title>
<link rel="stylesheet" href="https://fonts.googleapis.com/css2?family=Cinzel:wght@600&family=Didact+Gothic&display=swap">
<style>
  :root {
    --page: #ffffff;
    --panel: #fdfdfd;
    --edge: #e6e6e6;
    --maroon: #6b3131;
    --sun: #e6b223;
    --sky: #6886bd;
    --leaf: #2e9a48;
    --white: #ffffff;
  }
  * { margin: 0; padding: 0; box-sizing: border-box; }
  html, body { width: 1200px; height: 1200px; overflow: hidden; background: var(--page); }
  .canvas { position: relative; width: 1200px; height: 1200px; }

  .shopfront {
    position: absolute; left: 44px; top: 242px;
    width: 1096px; height: 553px;
    background: var(--panel);
    border: 1px solid var(--edge);
    overflow: hidden;
  }

  .brand {
    position: absolute; left: 0; top: 0; width: 100%; height: 366px;
    display: flex; align-items: center; justify-content: center; gap: 36px;
  }
  .brand-dot {
    width: 150px; height: 150px; border-radius: 50%;
    background: var(--leaf);
    flex: none;
  }
  .brand-name {
    font-family: "Cinzel", serif; font-weight: 600;
    color: var(--maroon);
    line-height: 1.05;
  }
  .brand-name .line-1 { display: block; font-size: 54px; }
  .brand-name .line-2 { display: block; font-size: 40px; padding-left: 40px; }

  .services-band {
    position: absolute; left: 0; top: 366px; width: 100%; height: 52px;
    background: var(--sun);
    display: flex; align-items: center; padding-left: 38px;
    font-family: "Didact Gothic", sans-serif; font-size: 25px;
    color: var(--white); letter-spacing: -1px;
  }
  .services-band .service { white-space: nowrap; }
  .services-band .sep {
    display: inline-block; width: 7px; height: 5px; border-radius: 50%;
    background: var(--white); margin: 0 10px; transform: translateY(2px);
  }

  .message-band {
    position: absolute; left: 0; top: 418px; width: 100%; height: 135px;
    background: var(--sky);
    padding: 30px 0 0 38px;
    font-family: "Didact Gothic", sans-serif; font-size: 27px;
    color: var(--white); letter-spacing: -0.6px;
  }
  .message-band p { line-height: 45px; }

  .leaf-decor {
    position: absolute; right: 0; top: 366px;
    width: 440px; height: 187px;
    background: linear-gradient(100deg, rgba(255,255,255,0) 0%, rgba(255,255,255,0.35) 45%, rgba(255,255,255,0.7) 100%);
  }
</style>
</head>
<body>
<div class="canvas">
  <section class="shopfront">
    <header class="brand">
      <div class="brand-dot"></div>
      <h1 class="brand-name">
        <span class="line-1">Bright Harbour</span>
        <span class="line-2">Care Services</span>
      </h1>
    </header>

    <div class="services-band">
      <span class="service">Travel</span><span class="sep"></span>
      <span class="service">Cleaning</span><span class="sep"></span>
      <span class="service">Accommodation</span><span class="sep"></span>
      <span class="service">Shopping</span><span class="sep"></span>
      <span class="service">Everyday household tasks</span>
    </div>

    <div class="message-band">
      <p>We are people helping People.</p>
      <p>Supporting you to live the life you want to live</p>
    </div>

    <div class="leaf-decor" role="img" aria-label="Drifting white leaves decoration"></div>
  </section>
</div>
</body>
</html>
```